Personal informs intake and New Zealand divorce form automated filling service

I need a website that has a professional appearance, take information from clients, automatically fill New Zealand divorce forms based on information gathered. The personal information are listed:
Applicant’s information

1 First name

2 Middle name ( if Any )

3 Last name

4 Date of birth

5 Address

6 Email

7 Gender

8 Mobile

9 Occupation

10 Ethnicity

11 Country of residence

12 Do you live in New Zealand permanently?

13 Do you and your spouse have children who are under age 16 who require additional care?

Spouse’s information

1 Spouse’s first name

2 Spouse’s middle name ( if any )

3 Spouse’s last name

4 Spouse’s date of birth

5 Spouse’s occupation

6 Spouse’s ethnicity

7 Mobil number

8 Address

Marriage details

1 Did either party change their name by deed poll following the marriage/ civil union.

2 Date of marriage

3 Place and Address where the marriage was solemnized?

4 What date did you start living together?

5 What date did you cease living together?

6 How did you agree to separate? ( verbal agreement, written agreement, court order, or other )

The forms are New Zealand one party/joint application for Order dissolving a marriage or civil union.
Once the forms are completed, it will be checked by a human before sending to the paid clients by email. The website needs to integrate multiple mainstream payment options.

The forms are uploaded, please view it and set up the questionnaire accordingly to ensure all questions in the forms are answered. Must be able to distinguish one party or joint application.

Please contact me if you are interested and need more information.

Updated an AI generated draft as a sample

Target Market(s)

Divorcées

Coding

Coded - Design and coding required

Number of Pages Required

1 page

Font styles to use
Sans Serif

Colors

Designer to choose colors to be used in the design.

Requirements
Must have
• A professional appearance, easy to initiate the information intake process
Nice to have
• Step by step guideline, easy to understand how the website works
Should not have
• Bright colors

```html
<!DOCTYPE html>
<html lang="en">
<head>
<meta charset="utf-8">
<title>Dissolution Application Intake</title>
<link href="https://fonts.googleapis.com/css2?family=Libre+Caslon+Text:wght@700&family=Lato:wght@400;700&display=swap" rel="stylesheet">
<style>
:root{
  --page:#f4f9fd;
  --card:#ffffff;
  --navy:#0b4a92;
  --sky:#0a8fd1;
  --line:#bfc6cf;
  --label:#3b3f45;
  --hint:#a3b6d3;
  --choice:#2b5ca6;
}
*{box-sizing:border-box;margin:0;padding:0}
html,body{width:1200px;height:2405px;overflow:hidden}
body{background:var(--page);font-family:"Lato",sans-serif;position:relative}
.brand{position:absolute;left:500px;top:57px;width:200px;height:66px;display:flex;align-items:center;justify-content:center;gap:8px}
.brand-mark{width:14px;height:14px;background:var(--sky)}
.brand-name{font-family:"Lato",sans-serif;font-weight:700;font-size:15px;color:var(--navy);letter-spacing:.5px}
.mode-tab{position:absolute;top:179px;width:265px;height:59px;border:2px solid;background:transparent;
  font-family:"Libre Caslon Text",serif;font-weight:700;font-size:19px;letter-spacing:.8px;display:flex;align-items:center;justify-content:center}
.mode-tab.one{left:313px;border-color:var(--sky);color:var(--sky)}
.mode-tab.joint{left:622px;border-color:var(--navy);color:var(--navy)}
.card{position:absolute;left:112px;width:976px;background:var(--card);box-shadow:0 0 6px rgba(20,50,90,.08);padding:36px 53px 0 48px}
.card h2{font-family:"Libre Caslon Text",serif;font-weight:700;font-size:29px;color:var(--navy);letter-spacing:1px;line-height:1;margin-bottom:36px}
.applicant{top:297px;height:701px}
.spouse{top:1055px;height:456px}
.marriage{top:1571px;height:619px}
.grid{display:flex;flex-wrap:wrap;column-gap:12px;row-gap:28px}
.field{position:relative;width:431px;height:57px;border:1px solid var(--line)}
.field.wide{width:876px}
.field.short{width:282px}
.field.mid{width:577px}
.field.tall{height:148px}
.field legend,.field .label{position:absolute;top:-10px;left:20px;background:var(--card);padding:0 8px;font-size:15px;color:var(--label);line-height:18px;white-space:nowrap}
.hint{position:absolute;left:29px;top:20px;font-size:15px;color:var(--hint)}
.chevron{position:absolute;right:28px;top:24px}
.choices{position:absolute;left:33px;top:23px;display:flex;gap:0;font-size:15px;color:var(--choice)}
.choice{display:flex;align-items:center;gap:6px}
.choice i{display:inline-block;width:11px;height:11px;border:1.5px solid var(--choice);border-radius:2px}
.action{position:absolute;top:2249px;width:168px;height:60px;color:#fff;border:none;
  font-family:"Libre Caslon Text",serif;font-weight:700;font-size:18px;letter-spacing:.8px;display:flex;align-items:center;justify-content:center}
.action.submit{left:160px;background:var(--sky)}
.action.save{left:366px;background:var(--navy)}
</style>
</head>
<body>

<div class="brand"><span class="brand-mark"></span><span class="brand-name">Office of Family Records</span></div>

<div class="mode-tab one">ONE PARTY</div>
<div class="mode-tab joint">JOINT APPLICATION</div>

<section class="card applicant">
  <h2>APPLICANT’S INFORMATION</h2>
  <div class="grid">
    <div class="field"><span class="label">First name</span><span class="hint">John</span></div>
    <div class="field"><span class="label">Middle name ( if Any )</span><span class="hint">Vinynl</span></div>
    <div class="field"><span class="label">Last name</span><span class="hint">Doe</span></div>
    <div class="field"><span class="label">Date of birth</span><span class="hint">DD-MM-YY</span></div>
    <div class="field"><span class="label">Address</span><span class="hint">Address Information</span></div>
    <div class="field"><span class="label">Email</span><span class="hint" style="top:26px">info@email.com</span></div>
    <div class="field"><span class="label">Gender</span>
      <div class="choices"><span class="choice" style="width:118px"><i></i>Male</span><span class="choice" style="width:129px"><i></i>Female</span><span class="choice"><i></i>Other</span></div></div>
    <div class="field"><span class="label">Mobile</span><span class="hint" style="top:17px">+1 888 **** ***</span></div>
    <div class="field"><span class="label">Occupation</span>
      <svg class="chevron" width="12" height="8" viewBox="0 0 12 8"><path d="M1.5 1.5 6 6l4.5-4.5" fill="none" stroke="#333" stroke-width="2"/></svg></div>
    <div class="field"><span class="label">Ethnicity</span><span class="hint">Lorem Ipsum</span></div>
    <div class="field"><span class="label">Country of Residence</span>
      <svg class="chevron" width="12" height="8" viewBox="0 0 12 8"><path d="M1.5 1.5 6 6l4.5-4.5" fill="none" stroke="#333" stroke-width="2"/></svg></div>
    <div class="field"><span class="label">Do you live in New Zealand permanently?</span>
      <div class="choices" style="left:36px"><span class="choice" style="width:118px"><i></i>Yes</span><span class="choice"><i></i>No</span></div></div>
    <div class="field wide"><span class="label">Do you and your spouse have children who are under age 16 who require additional care?</span>
      <div class="choices"><span class="choice" style="width:118px"><i></i>Yes</span><span class="choice"><i></i>No</span></div></div>
  </div>
</section>

<section class="card spouse">
  <h2>SPOUSE’S INFORMATION</h2>
  <div class="grid">
    <div class="field"><span class="label">Spouse’s first name</span><span class="hint">John</span></div>
    <div class="field"><span class="label">Spouse’s middle name ( if any )</span><span class="hint">Vinynl</span></div>
    <div class="field"><span class="label">Spouse’s last name</span><span class="hint">Doe</span></div>
    <div class="field"><span class="label">Spouse’s date of birth</span><span class="hint">DD-MM-YY</span></div>
    <div class="field"><span class="label">Spouse’s Occupation</span>
      <svg class="chevron" width="12" height="8" viewBox="0 0 12 8"><path d="M1.5 1.5 6 6l4.5-4.5" fill="none" stroke="#333" stroke-width="2"/></svg></div>
    <div class="field"><span class="label">Spouse’s ethnicity</span><span class="hint">Lorem Ipsum</span></div>
    <div class="field"><span class="label">Spouse’s address</span><span class="hint">Address Information</span></div>
    <div class="field"><span class="label">Spouse’s email</span><span class="hint" style="top:23px">info@email.com</span></div>
  </div>
</section>

<section class="card marriage">
  <h2>MARRIAGE DETAILS</h2>
  <div class="grid">
    <div class="field wide"><span class="label">Did either party change their name by deed poll following the marriage/ civil union</span><span class="hint">Text Here.....</span></div>
    <div class="field short"><span class="label">Date of marriage</span>
      <div class="choices"><span class="choice" style="width:118px"><i></i>Yes</span><span class="choice"><i></i>No</span></div></div>
    <div class="field mid"><span class="label">What date did you start living together?</span><span class="hint">Text Here.....</span></div>
    <div class="field wide tall"><span class="label">Place and Address where the marriage was solemnized?</span><span class="hint">Text Here.....</span></div>
    <div class="field wide"><span class="label">What date did you cease living together?</span><span class="hint">Text Here.....</span></div>
    <div class="field wide"><span class="label">How did you agree to separate?</span>
      <div class="choices"><span class="choice" style="width:176px"><i></i>Verbal agreement</span><span class="choice" style="width:186px"><i></i>Written agreement</span><span class="choice" style="width:138px"><i></i>Court order</span><span class="choice"><i></i>Other</span></div></div>
  </div>
</section>

<div class="action submit">SUBMIT</div>
<div class="action save">SAVE</div>

</body>
</html>
```